BUSINESS CARD - HALVERDINE RURAL SERVICES

I would like to create a business card for my fertilizer spreading business. I would like to incorporate my existing logo and also a description of the services offered. The business card will be given to farmers so must be kept simple but effective. It will also be left in stores so much also be eye catching in order to stand out from other cards.

Target Market(s)

FARMERS

Requirements
Must have
• FRONT OF CARD = EXISTING LOGO + "CUSTOMISED SPREADING" below the logo

REAR Of CARD = SERVICES OFFERED AND CONTACT DETAILS

- Bulk fertilizer including Lime, Gypsum, Manure & Compost
- Granular fertilizer including Single Super, Urea, Gran-am, & Custom Blends
- Modern equipment - Autosteer & Variable Rate Capable
- Friendly & Reliable Service
- Contact Gus: 0471 502 318
Nice to have
• utilize same color scheme as existing logo

```html
<!DOCTYPE html>
<html lang="en">
<head>
<meta charset="utf-8">
<title>Halverdine Rural Services – Business Card</title>
<link rel="stylesheet" href="https://fonts.googleapis.com/css2?family=Montserrat:wght@400;600&display=swap">
<style>
  :root {
    --page: #ececec;
    --card-white: #ffffff;
    --card-grey: #58585a;
    --ink: #58585a;
    --ink-soft: #666668;
    --orange: #f7941d;
    --silver: #d8d8da;
    --white: #ffffff;
  }
  * { box-sizing: border-box; margin: 0; padding: 0; }
  html, body {
    width: 1200px; height: 1200px; overflow: hidden;
    background: var(--page);
    font-family: "Montserrat", sans-serif;
  }
  .card {
    position: absolute; left: 200px;
    width: 800px; height: 457px;
    border-radius: 26px; overflow: hidden;
    box-shadow: 0 10px 24px rgba(0,0,0,.18);
  }
  .card--front { top: 92px; background: var(--card-white); }
  .card--back { top: 650px; background: var(--card-grey); }

  /* front */
  .brand {
    position: absolute; left: 70px; top: 110px; width: 280px;
    text-align: center;
  }
  .brand__mark { display: block; margin: 0 auto 12px; }
  .brand__name {
    font-weight: 600; font-size: 25px; line-height: 29px;
    color: var(--ink); letter-spacing: -0.2px;
  }
  .brand__tagline {
    margin-top: 8px; font-weight: 400; font-size: 16px;
    letter-spacing: 2px; color: var(--ink);
  }
  .divider {
    position: absolute; left: 368px; top: 97px;
    width: 1px; height: 227px; background: var(--ink);
  }
  .services {
    position: absolute; left: 403px; top: 98px; width: 340px;
    list-style: none;
  }
  .services li {
    position: relative; padding-left: 20px; margin-bottom: 23px;
    font-size: 16.5px; line-height: 22px; color: var(--ink-soft);
  }
  .services li::before {
    content: ""; position: absolute; left: 0; top: 7px;
    width: 7px; height: 7px; border-radius: 50%; background: var(--orange);
  }
  .contact-bar {
    position: absolute; left: 0; top: 380px; width: 800px; height: 42px;
    background: var(--ink);
  }
  .contact-bar__accent {
    position: absolute; right: 0; top: 0; width: 162px; height: 42px;
    background: var(--orange);
  }
  .contact-bar__text {
    position: absolute; left: 41px; top: 0; line-height: 42px;
    font-size: 16.5px; color: var(--white);
  }
  .contact-bar__dot { position: absolute; left: 604px; top: -2px; }

  /* back */
  .back-brand {
    position: absolute; left: 0; top: 108px; width: 800px; text-align: center;
  }
  .back-brand__mark { display: block; margin: 0 auto 16px; }
  .back-brand__name {
    font-weight: 600; font-size: 36px; line-height: 42px;
    color: var(--silver); letter-spacing: -0.3px;
  }
  .back-brand__tagline {
    margin-top: 10px; font-size: 21px; letter-spacing: 2.6px;
    color: var(--silver);
  }
</style>
</head>
<body>
  <section class="card card--front">
    <div class="brand">
      <svg class="brand__mark" width="118" height="118" viewBox="0 0 118 118" aria-hidden="true">
        <circle cx="59" cy="59" r="59" fill="var(--ink)"/>
      </svg>
      <p class="brand__name">Halverdine Rural Services</p>
      <p class="brand__tagline">CUSTOMISED SPREADING</p>
    </div>

    <div class="divider"></div>

    <ul class="services">
      <li>Bulk fertilizer including Lime,<br>Gypsum, Manure &amp; Compost</li>
      <li>Granular fertilizer including Single<br>Super, Urea, Gran-am, &amp; Custom Blends</li>
      <li>Modern equipment -<br>Autosteer &amp; Variable Rate Capable</li>
      <li>Friendly &amp; Reliable Service</li>
    </ul>

    <div class="contact-bar">
      <div class="contact-bar__accent"></div>
      <p class="contact-bar__text">0471 502 318 | info@halverdinerural.com | halverdinerural.com</p>
      <svg class="contact-bar__dot" width="46" height="46" viewBox="0 0 46 46" aria-hidden="true">
        <circle cx="23" cy="23" r="21" fill="var(--ink)" stroke="var(--white)" stroke-width="2.5"/>
      </svg>
    </div>
  </section>

  <section class="card card--back">
    <div class="back-brand">
      <svg class="back-brand__mark" width="146" height="146" viewBox="0 0 146 146" aria-hidden="true">
        <circle cx="73" cy="73" r="73" fill="var(--silver)"/>
      </svg>
      <p class="back-brand__name">Halverdine Rural Services</p>
      <p class="back-brand__tagline">CUSTOMISED SPREADING</p>
    </div>
  </section>
</body>
</html>
```